Powerpoint Template for a cool IT Recruiting and Consulting Company

We need to have a PowerPoint template designed for our company. We are a Technology Consulting and Recruiting company in Canada.

I'm not looking for an explosion of colours, stay elegant and sharp.

The message that it needs to portray a cool tech company utilizing the blue in our logo but also professionalism and an excitement feel about it that makes clients want to do business with us.

I have attached 2 screenshots of the logo options and also the PDF of them.

Looking forward to seeing the results.

Target Market(s)

We sell our services to Banks, Government and other Tech Companies

Industry/Entity Type

It Service

Font styles to use
Sans Serif

Colors
0592cd

Requirements
Must have
• Logo
Nice to have
• N/A
Should not have
• Lots of colours

```html
<!DOCTYPE html>
<html lang="en">
<head>
<meta charset="utf-8">
<title>Vantyx Presentation Template</title>
<link href="https://fonts.googleapis.com/css2?family=Roboto:wght@300;400;500;700&family=Oswald:wght@500;600&display=swap" rel="stylesheet">
<style>
:root{
  --blue:#3f6f9c;
  --blue-dark:#2f5d88;
  --blue-light:#5a86b0;
  --ink:#111;
  --text:#333;
  --page:#fff;
  --shadow:rgba(0,0,0,.18);
  --ring:#eceef1;
}
*{box-sizing:border-box;margin:0;padding:0}
html,body{width:1200px;height:758px;overflow:hidden;background:var(--page);font-family:"Roboto",Arial,sans-serif}
.board{position:relative;width:1200px;height:758px}
.slide{position:absolute;width:568px;height:318px;background:#fff;box-shadow:0 1px 4px var(--shadow);overflow:hidden}
.caption{position:absolute;width:568px;text-align:center;font:700 18px "Roboto",Arial,sans-serif;color:var(--ink);letter-spacing:.3px}
.photo{position:absolute}
.brand{position:absolute;display:flex;align-items:center;gap:4px;color:var(--blue);font-weight:500;font-size:12px}
.brand .dot{width:9px;height:9px;border-radius:50%;border:1.6px solid var(--blue)}
.title{position:absolute;line-height:1}
.title .t1{display:block;font-weight:700;font-size:30px;color:var(--ink)}
.title .t2{display:block;font-weight:300;font-size:30px;color:var(--blue);margin-top:1px}
.title .rule{display:block;width:68px;height:2px;background:var(--blue);margin-top:8px}
.body{position:absolute;font-size:7.2px;line-height:11.2px;color:var(--text);text-align:justify}
.body em{font-style:normal;color:var(--blue)}
.footer{position:absolute;left:0;top:282px;height:14px;width:240px;background:linear-gradient(90deg,var(--blue-dark),var(--blue-light));color:#fff;font-size:6.4px;letter-spacing:1.3px;line-height:14px;padding-left:66px}
.footer-mark{position:absolute;top:279px;left:244px;width:20px;height:20px;border-radius:50%;border:2px solid var(--blue)}
.page-no{position:absolute;top:286px;left:532px;font-size:6.4px;color:var(--ink)}
/* cover */
.cover-box{position:absolute;left:21px;top:50px;width:205px;height:220px;border-radius:4px;background:linear-gradient(180deg,#3d6e9c,#4b7ba8);color:#fff;text-align:center}
.cover-brand{display:flex;align-items:center;justify-content:center;gap:7px;margin-top:20px;font-weight:500;font-size:32px}
.cover-brand .dot{width:20px;height:20px;border-radius:50%;border:3px solid #fff}
.cover-title{font-family:"Oswald",sans-serif;font-weight:600;font-size:22px;line-height:29px;margin-top:15px;letter-spacing:.3px}
.cover-sub{font-size:14px;font-weight:300;margin-top:6px}
.cover-line{width:172px;height:1px;background:rgba(255,255,255,.7);margin:14px auto 5px}
.cover-note{font-size:10px;font-weight:300}
/* page 02 card */
.card{position:absolute;left:390px;top:130px;width:166px;height:102px;background:#fff;border:1px solid var(--blue);border-radius:8px;padding:8px 10px}
.card h3{font-weight:400;font-size:12px;color:var(--blue);margin-bottom:6px}
.card p{font-size:6.6px;line-height:11.2px;color:var(--text);text-align:justify}
.card em{font-style:normal;color:var(--blue)}
/* page 03 */
.hero-text{position:absolute;left:9px;bottom:10px;color:#fff;font-weight:700;font-size:22px;line-height:28px;letter-spacing:.4px}
.step{position:absolute;width:80px;font-size:6.4px;line-height:10px;color:var(--text)}
.step b{display:block;color:var(--blue);font-weight:500;font-size:6.6px}
.step.left{text-align:right}
.hub-brand{position:absolute;left:334px;top:141px;width:80px;text-align:center;color:var(--blue);font-weight:500;font-size:14px}
.hub-brand .dot{display:block;margin:0 auto 3px;width:20px;height:20px;border-radius:50%;border:2.4px solid var(--blue)}
</style>
</head>
<body>
<main class="board">

  <!-- Cover -->
  <section class="slide" style="left:16px;top:16px">
    <div class="photo" role="img" aria-label="Photo of a team meeting in a bright office" style="left:206px;top:0;width:362px;height:318px;background:linear-gradient(160deg,#d9dde0 0%,#b9bfc4 40%,#7c7570 70%,#4a4a4f 100%)"></div>
    <div class="cover-box">
      <div class="cover-brand"><span class="dot"></span>Vantyx</div>
      <div class="cover-title">PRESENTATION<br>TITLE</div>
      <div class="cover-sub">Sub - title goes here</div>
      <div class="cover-line"></div>
      <div class="cover-note">Lorem Ipsum is simply dummy text</div>
    </div>
  </section>
  <div class="caption" style="left:16px;top:348px">COVER PAGE</div>

  <!-- Page 01 -->
  <section class="slide" style="left:615px;top:16px">
    <div class="brand" style="left:484px;top:22px"><span class="dot"></span>Vantyx</div>
    <div class="title" style="left:55px;top:65px"><span class="t1">Lorem</span><span class="t2">Ipsum Text</span><span class="rule"></span></div>
    <p class="body" style="left:55px;top:154px;width:175px"><em>Lorem Ipsum is simply dummy</em> text of the printing and typesetting industry. Lorem Ipsum has been the industry's standard dummy text ever since the 1500s, when an unknown printer took a galley of type and scrambled it to make a type specimen book. It has survived not only five centuries. But also the leap into electronic typesetting, remaining essentially unchanged. It was popularised in the 1960s with the release of Letraset sheets containing.</p>
    <div class="photo" role="img" aria-label="Photo of a hand writing notes beside a laptop" style="left:251px;top:50px;width:317px;height:218px;border-radius:6px 0 0 6px;background:linear-gradient(135deg,#4d6a8c 0%,#7b8ea3 35%,#c7c3bb 60%,#3a3d44 100%)"></div>
    <div class="footer">www.vantyxconsult.com</div>
    <div class="footer-mark"></div>
    <div class="page-no">01</div>
  </section>
  <div class="caption" style="left:615px;top:348px">PAGE - 01</div>

  <!-- Page 02 -->
  <section class="slide" style="left:16px;top:391px">
    <div class="title" style="left:54px;top:45px"><span class="t1">Lorem</span><span class="t2">Ipsum Text</span><span class="rule"></span></div>
    <p class="body" style="left:55px;top:134px;width:176px"><em>Lorem Ipsum is simply dummy</em> text of the printing and typesetting industry. Lorem Ipsum has been the industry's standard dummy text ever since the 1500s, when an unknown printer took a galley of type and scrambled it to make a type specimen book. It has survived not only five centuries. But also the leap into electronic typesetting, remaining essentially unchanged. It was popularised in the 1960s with the release of Letraset sheets containing.</p>
    <div class="photo" role="img" aria-label="Photo of a woman working on a laptop at a wooden table" style="left:248px;top:0;width:210px;height:266px;border-radius:0 0 8px 8px;background:linear-gradient(180deg,#5a4a44 0%,#9a7d6c 35%,#e2ddd6 55%,#c98a4e 75%,#b06e34 100%)"></div>
    <div class="brand" style="left:484px;top:22px"><span class="dot"></span>Vantyx</div>
    <div class="card">
      <h3>Lorem Ipsum</h3>
      <p><em>Lorem Ipsum is simply dummy</em> text of the printing and typesetting industry. Lorem Ipsum has been the industry's standard dummy text ever since the 1500s, when an unknown printer took.</p>
    </div>
    <div class="footer">www.vantyxconsult.com</div>
    <div class="footer-mark"></div>
    <div class="page-no">02</div>
  </section>
  <div class="caption" style="left:16px;top:723px">PAGE - 02</div>

  <!-- Page 03 -->
  <section class="slide" style="left:615px;top:391px">
    <div class="photo" role="img" aria-label="Photo of a hand writing with a pen, tinted blue" style="left:24px;top:0;width:175px;height:263px;border-radius:0 0 8px 8px;background:linear-gradient(180deg,#6e89a8 0%,#8a9db0 35%,#4f76a0 70%,#3c6a99 100%)">
      <div class="hero-text">Lorem Ipsum<br>Simply Text<br>Typesetting</div>
    </div>
    <div class="brand" style="left:484px;top:22px"><span class="dot"></span>Vantyx</div>
    <svg style="position:absolute;left:0;top:0" width="568" height="318" viewBox="0 0 568 318">
      <circle cx="374" cy="153" r="76" fill="var(--ring)"/>
      <circle cx="374" cy="153" r="58" fill="#fff"/>
      <circle cx="374" cy="153" r="55" fill="#eef0f3"/>
      <g fill="none" stroke="#222" stroke-width=".8">
        <polyline points="288,79 327,79 327,99 336,99"/>
        <polyline points="290,143 307,143"/>
        <polyline points="288,208 318,208 318,188 328,188"/>
        <polyline points="460,79 421,79 421,99 412,99"/>
        <polyline points="458,143 441,143"/>
        <polyline points="460,208 430,208 430,188 420,188"/>
      </g>
      <g fill="var(--blue)">
        <circle cx="288" cy="79" r="1.3"/><circle cx="290" cy="143" r="1.3"/><circle cx="288" cy="208" r="1.3"/>
        <circle cx="460" cy="79" r="1.3"/><circle cx="458" cy="143" r="1.3"/><circle cx="460" cy="208" r="1.3"/>
      </g>
    </svg>
    <div class="hub-brand"><span class="dot"></span>Vantyx</div>
    <div class="step left" style="left:204px;top:74px"><b>STEP 01</b>Lorem Ipsum is simply dummy text of the.</div>
    <div class="step left" style="left:204px;top:138px"><b>STEP 02</b>Lorem Ipsum is simply dummy text of the.</div>
    <div class="step left" style="left:204px;top:203px"><b>STEP 03</b>Lorem Ipsum is simply dummy text of the.</div>
    <div class="step" style="left:464px;top:74px"><b>STEP 04</b>Lorem Ipsum is simply dummy text of the.</div>
    <div class="step" style="left:464px;top:138px"><b>STEP 05</b>Lorem Ipsum is simply dummy text of the.</div>
    <div class="step" style="left:464px;top:203px"><b>STEP 06</b>Lorem Ipsum is simply dummy text of the.</div>
    <div class="footer">www.vantyxconsult.com</div>
    <div class="footer-mark"></div>
    <div class="page-no">03</div>
  </section>
  <div class="caption" style="left:615px;top:723px">PAGE - 03</div>

</main>
</body>
</html>
```